TR Stationery - Modern Contemporary

Develop modern template for Letterhead and Stationery (business card, letterhead, envelopes) using the TR Logo and Icon

Colors
0054AA
0677BA
7BADD7
CADEEF
E8F1F8
00AB8E
00BBA5
67D7C9
C6EFE9
E9F9F6
EE7325
F08F49
F5BC92
FAE3D3
FDF4ED
6B429C
8869AF
B7A5CE
E3DAEB
F3F0F8

```html
<!DOCTYPE html>
<html lang="en">
<head>
<meta charset="utf-8">
<title>TR Stationery – Stationery Set</title>
<link rel="stylesheet" href="https://fonts.googleapis.com/css2?family=Roboto:wght@300;400;500;700;900&family=Pinyon+Script&display=swap">
<style>
  :root{
    --bg:#e6e6e6;
    --paper:#f6f8fa;
    --ink:#0054AA;
    --text:#3a3f47;
    --accent:#EE7325;
    --accent-soft:#F5BC92;
    --teal:#00AB8E;
    --deep:#0054AA;
    --mid:#0677BA;
    --sky:#7BADD7;
    --rule:#B7A5CE;
  }
  *{box-sizing:border-box;margin:0;padding:0}
  html,body{width:1200px;height:942px;overflow:hidden}
  body{background:var(--bg);font-family:"Roboto",Arial,sans-serif;color:var(--text);position:relative}
  .sheet{position:absolute;background:var(--paper);box-shadow:0 3px 10px rgba(0,0,0,.12);overflow:hidden}

  .brand{display:flex;align-items:center;gap:.35em;font-weight:900;color:var(--ink);white-space:nowrap;line-height:1}
  .brand__square{display:inline-block;width:.7em;height:.7em;background:var(--accent)}

  .swoosh{position:absolute;left:0;bottom:0;width:100%;display:block}

  .contact{position:absolute;display:flex;align-items:flex-end}
  .contact__list{list-style:none}
  .contact__list li{display:flex;align-items:center;gap:.55em;white-space:nowrap}
  .contact__list svg{width:.8em;height:.8em;fill:var(--accent);flex:none}
  .contact__divider{width:1px;height:26.7px;background:var(--rule);margin:0 .9em}
  .contact__company{white-space:nowrap;font-weight:400}
  .contact__company strong{display:block;color:var(--mid);font-weight:400}

  /* letterhead */
  .letterhead{left:157px;top:150px;width:437px;height:618px}
  .letterhead .brand{position:absolute;left:30px;top:36px;font-size:13px}
  .letterhead .contact{left:180px;top:31px;font-size:7.2px;line-height:8.9px}
  .letter{position:absolute;left:46px;top:146px;width:344px;font-size:7.4px;line-height:10.3px;font-weight:300;color:var(--text)}
  .letter p{margin-bottom:10.3px;text-align:justify}
  .letter .letter__date,.letter .letter__address,.letter .letter__salutation{text-align:left}
  .letter__address{margin-bottom:14px!important}
  .letter__closing{margin-top:30px;text-align:left;margin-bottom:0!important}
  .letter__signature{font-family:"Pinyon Script",cursive;font-size:14px;line-height:18px;color:var(--deep);margin-top:2px}

  /* business card */
  .card-front{left:625px;top:139px;width:228px;height:130px}
  .card-front .brand{position:absolute;left:17px;top:58px;font-size:11px}
  .card__divider{position:absolute;left:114px;top:28px;width:1px;height:72px;background:var(--rule)}
  .card__details{position:absolute;left:123px;top:27px;font-size:4.4px;line-height:6.3px}
  .card__name{color:var(--mid);font-weight:500;font-size:6.6px;line-height:7px}
  .card__role{font-size:4.4px;margin-bottom:5px}
  .card__details .contact__list svg{width:4px;height:4px}
  .card__details .contact__list li{gap:3px}
  .card__company{margin-top:4px;font-size:4.6px;line-height:6.3px}
  .card__company strong{display:block;color:var(--mid);font-weight:400}

  .card-back{left:897px;top:139px;width:227px;height:130px;background:var(--deep);display:flex;align-items:center;justify-content:center}
  .card-back .brand{font-size:26px;color:var(--sky)}

  /* envelope front */
  .envelope-front{left:624px;top:298px;width:502px;height:217px}
  .envelope-front .brand{position:absolute;left:37px;top:40px;font-size:13px}
  .envelope-front .contact{left:37px;top:128px;font-size:7.2px;line-height:8.9px}

  /* envelope back */
  .envelope-back{left:624px;top:550px;width:502px;height:218px}
  .envelope-back__body{position:absolute;inset:0;display:block}
  .envelope-back__flap{fill:var(--deep)}
  .envelope-back__fold{stroke:#d3dbe3;stroke-width:1;fill:none}
  .envelope-back .brand{position:absolute;left:0;right:0;top:26px;justify-content:center;font-size:18px;color:var(--accent-soft)}

  .swoosh__accent{fill:var(--accent)}
  .swoosh__base{fill:var(--deep)}
</style>
</head>
<body>

<svg width="0" height="0" style="position:absolute" aria-hidden="true">
  <defs>
    <symbol id="icon-phone" viewBox="0 0 24 24"><path d="M6.6 10.8a15.1 15.1 0 0 0 6.6 6.6l2.2-2.2a1 1 0 0 1 1-.25 11.4 11.4 0 0 0 3.6.57 1 1 0 0 1 1 1V20a1 1 0 0 1-1 1A17 17 0 0 1 3 4a1 1 0 0 1 1-1h3.5a1 1 0 0 1 1 1c0 1.25.2 2.45.57 3.6a1 1 0 0 1-.25 1z"/></symbol>
    <symbol id="icon-mail" viewBox="0 0 24 24"><path d="M2 5h20v14H2zm2 2v.5l8 5 8-5V7l-8 5z"/></symbol>
    <symbol id="icon-web" viewBox="0 0 24 24"><path d="M12 2a10 10 0 1 0 0 20 10 10 0 0 0 0-20zm6.9 6h-3a15 15 0 0 0-1.4-3.6A8 8 0 0 1 18.9 8zM12 4c.8 1.2 1.5 2.5 1.9 4h-3.8c.4-1.5 1.1-2.8 1.9-4zM4.3 14a8 8 0 0 1 0-4h3.4a16 16 0 0 0 0 4zm.8 2h3a15 15 0 0 0 1.4 3.6A8 8 0 0 1 5.1 16zm3-8h-3a8 8 0 0 1 4.4-3.6A15 15 0 0 0 8.1 8zM12 20c-.8-1.2-1.5-2.5-1.9-4h3.8c-.4 1.5-1.1 2.8-1.9 4zm2.3-6H9.7a14 14 0 0 1 0-4h4.6a14 14 0 0 1 0 4zm.2 5.6a15 15 0 0 0 1.4-3.6h3a8 8 0 0 1-4.4 3.6zm1.8-5.6a16 16 0 0 0 0-4h3.4a8 8 0 0 1 0 4z"/></symbol>
    <symbol id="swoosh" viewBox="0 0 100 20" preserveAspectRatio="none">
      <path class="swoosh__accent" d="M0 2 Q50 12 100 0 L100 0.6 Q50 15 0 8 Z"/>
      <path class="swoosh__base" d="M0 11 Q50 18 100 1.4 L100 20 L0 20 Z"/>
    </symbol>
  </defs>
</svg>

<!-- Letterhead -->
<section class="sheet letterhead">
  <div class="brand"><span class="brand__square"></span>TR Stationery</div>
  <div class="contact">
    <ul class="contact__list">
      <li><svg><use href="#icon-phone"/></svg>+86-21-55501210</li>
      <li><svg><use href="#icon-phone"/></svg>+86-21-55501211</li>
      <li><svg><use href="#icon-phone"/></svg>+86-21-55501298</li>
      <li><svg><use href="#icon-mail"/></svg>service@tr-pen.com</li>
      <li><svg><use href="#icon-web"/></svg>www.tr-pen.com</li>
    </ul>
    <span class="contact__divider"></span>
    <div class="contact__company">
      <strong>Shanghai TR Stationery Inc.</strong>
      No. 1280 Meiyuan Road<br>Riverside District, Shanghai, China
    </div>
  </div>

  <article class="letter">
    <p class="letter__date">01 January 2050</p>
    <p class="letter__address">Company (Pvt) Ltd.<br>PO Box 3355 Mainville St<br>Sample City Country 3355</p>
    <p class="letter__salutation">Dear Mark Ellison,</p>
    <p>Lorem ipsum dolor sit amet, consectetuer adipiscing elit, sed diam nonummy nibh euismod tincidunt ut laoreet dolore magna aliquam erat volutpat. Ut wisi enim ad minim veniam, quis nostrud exerci tation ullamcorper suscipit lobortis nisl ut aliquip ex ea commodo consequat. Duis dolore te feugait nulla facilisi. Nam liber tempor cum soluta nobis eleifend option congue nihil imperdiet doming id quod mazim placerat facer possim assum. Lorem ipsum dolor sit amet, consectetuer adipiscing elit, sed diam nonummy nibh euismod tincidunt ut laoreet dolore magna aliquam erat volutpat. Ut wisi enim ad minim veniam, quis nostrud exerci tation ullamcorper suscipit lobortis nisl ut aliquip ex ea commodo consequat.</p>
    <p>Consectetuer adipiscing elit, sed diam nonummy nibh euismod tincidunt ut laoreet dolore magna aliquam erat volutpat. Ut wisi enim ad minim veniam, quis nostrud exerci tation ullamcorper suscipit lobortis nisl ut aliquip ex ea commodo consequat. Consectetuer adipiscing elit, sed diam nonummy nibh euismod tincidunt ut laoreet dolore magna aliquam erat volutpat. Ut wisi enim ad minim veniam, quis nostrud exerci tation ullamcorper suscipit lobortis nisl ut aliquip ex ea commodo consequat.</p>
    <p>Consectetuer adipiscing elit, sed diam nonummy nibh euismod tincidunt ut laoreet dolore magna aliquam erat volutpat. Ut wisi enim ad minim veniam, quis nostrud exerci tation ullamcorper suscipit lobortis nisl ut aliquip ex ea commodo consequat. Consectetuer adipiscing elit, sed diam nonummy nibh euismod tincidunt ut laoreet dolore magna aliquam erat volutpat. Ut wisi enim ad minim veniam, quis nostrud exerci tation ullamcorper suscipit lobortis nisl ut aliquip ex ea commodo consequat.</p>
    <p class="letter__closing">Sincerely Yours</p>
    <div class="letter__signature">Daniel Hartwell</div>
  </article>

  <svg class="swoosh" style="height:50px"><use href="#swoosh" width="100%" height="100%"/></svg>
</section>

<!-- Business card front -->
<section class="sheet card-front">
  <div class="brand"><span class="brand__square"></span>TR Stationery</div>
  <span class="card__divider"></span>
  <div class="card__details">
    <div class="card__name">Lin Weiqiao</div>
    <div class="card__role">CEO</div>
    <ul class="contact__list">
      <li><svg><use href="#icon-phone"/></svg>+86-21-55501210</li>
      <li><svg><use href="#icon-phone"/></svg>+86-21-55501211</li>
      <li><svg><use href="#icon-phone"/></svg>+86-21-55501298</li>
      <li><svg><use href="#icon-mail"/></svg>service@tr-pen.com</li>
      <li><svg><use href="#icon-web"/></svg>www.tr-pen.com</li>
    </ul>
    <div class="card__company">
      <strong>Shanghai TR Stationery Inc.</strong>
      No. 1280 Meiyuan Road<br>Riverside District, Shanghai, China
    </div>
  </div>
  <svg class="swoosh" style="height:25px"><use href="#swoosh" width="100%" height="100%"/></svg>
</section>

<!-- Business card back -->
<section class="sheet card-back">
  <div class="brand">TR Stationery</div>
</section>

<!-- Envelope front -->
<section class="sheet envelope-front">
  <div class="brand"><span class="brand__square"></span>TR Stationery</div>
  <div class="contact">
    <ul class="contact__list">
      <li><svg><use href="#icon-phone"/></svg>+86-21-55501210</li>
      <li><svg><use href="#icon-phone"/></svg>+86-21-55501211</li>
      <li><svg><use href="#icon-phone"/></svg>+86-21-55501298</li>
      <li><svg><use href="#icon-mail"/></svg>service@tr-pen.com</li>
      <li><svg><use href="#icon-web"/></svg>www.tr-pen.com</li>
    </ul>
    <span class="contact__divider"></span>
    <div class="contact__company">
      <strong>Shanghai TR Stationery Inc.</strong>
      No. 1280 Meiyuan Road<br>Riverside District, Shanghai, China
    </div>
  </div>
  <svg class="swoosh" style="height:54px"><use href="#swoosh" width="100%" height="100%"/></svg>
</section>

<!-- Envelope back -->
<section class="sheet envelope-back">
  <svg class="envelope-back__body" viewBox="0 0 502 218" aria-hidden="true">
    <path class="envelope-back__fold" d="M8 218 L4 70 M494 218 L498 70"/>
    <path class="envelope-back__flap" d="M0 0 H502 L489 62 Q486 72 476 72 H26 Q16 72 13 62 Z"/>
  </svg>
  <div class="brand">TR Stationery</div>
</section>

</body>
</html>
```